Mabel's Fitness Business Cards

I would like my business cards to look expensive and sophisticated using my logo and the information below.

FRONT
Mabel’s Fitness logo

Tag line Become your happiest, healthiest and strongest self

Mabel Quint Harlow
Personal Trainer

e. mabel@mabelsfitstudio.example

t. 0781530462

w. www.mabelsfitstudio.example

```html
<!DOCTYPE html>
<html lang="en">
<head>
<meta charset="UTF-8">
<title>Mabel's Fitness Business Cards</title>
<link rel="stylesheet" href="https://fonts.googleapis.com/css2?family=Open+Sans:wght@400;600&display=swap">
<style>
  :root {
    --stage: #2b2b2b;
    --card-white: #ffffff;
    --card-black: #050505;
    --teal: #63b3bd;
    --taupe: #a79795;
    --ink: #1e1e1e;
    --divider: #8a8a8a;
  }
  * { box-sizing: border-box; margin: 0; padding: 0; }
  html, body {
    width: 1200px; height: 900px; overflow: hidden;
    background: var(--stage);
    font-family: "Open Sans", Arial, sans-serif;
  }
  .canvas {
    width: 1200px; height: 900px;
    display: flex; align-items: center; justify-content: center; gap: 44px;
  }
  .card {
    width: 520px; height: 300px;
    border-radius: 22px;
    position: relative; overflow: hidden;
    box-shadow: 0 14px 30px rgba(0,0,0,.45);
  }
  /* Contact side */
  .card-contact { background: var(--card-white); }
  .brand-block {
    position: absolute; left: 34px; top: 0; bottom: 0; width: 210px;
    display: flex; align-items: center; gap: 12px;
  }
  .brand-dot {
    width: 22px; height: 22px; border-radius: 50%;
    background: var(--teal); flex: none;
  }
  .brand-name {
    color: var(--teal); font-weight: 600; font-size: 24px; line-height: 1.15;
  }
  .divider {
    position: absolute; left: 262px; top: 78px; width: 1px; height: 140px;
    background: var(--divider);
  }
  .details { position: absolute; left: 280px; top: 84px; }
  .person-name {
    color: var(--teal); font-weight: 600; font-size: 18px; letter-spacing: .3px;
    text-transform: uppercase;
  }
  .person-role { color: var(--taupe); font-size: 14px; margin-bottom: 10px; }
  .contact-list { list-style: none; }
  .contact-item {
    display: flex; align-items: center; gap: 8px;
    color: var(--ink); font-size: 14px; line-height: 22px;
  }
  .contact-icon {
    width: 14px; height: 14px; border-radius: 2px; background: var(--teal);
    display: flex; align-items: center; justify-content: center; flex: none;
  }
  .contact-icon svg { width: 10px; height: 10px; }

  /* Brand side */
  .card-brand { background: var(--card-black); }
  .brand-mark {
    position: absolute; left: 0; right: 0; top: 74px;
    display: flex; align-items: center; justify-content: center; gap: 14px;
  }
  .brand-mark .brand-name { font-size: 30px; letter-spacing: 2px; text-transform: uppercase; }
  .tagline-band {
    position: absolute; left: 0; right: 0; bottom: 38px; height: 46px;
    background: var(--teal);
    display: flex; align-items: center; justify-content: center;
  }
  .tagline { color: #fff; font-weight: 600; font-size: 17px; }
</style>
</head>
<body>
<main class="canvas">
  <section class="card card-contact" aria-label="Business card, contact side">
    <div class="brand-block">
      <span class="brand-dot"></span>
      <span class="brand-name">Mabel’s Fitness</span>
    </div>
    <div class="divider"></div>
    <div class="details">
      <h1 class="person-name">Mabel Quint Harlow</h1>
      <p class="person-role">Personal Trainer</p>
      <ul class="contact-list">
        <li class="contact-item">
          <span class="contact-icon"><svg viewBox="0 0 10 10"><rect x="3" y="1" width="4" height="8" rx="1" fill="none" stroke="#fff" stroke-width="1.2"/></svg></span>
          0781530462
        </li>
        <li class="contact-item">
          <span class="contact-icon"><svg viewBox="0 0 10 10"><rect x="1" y="2.5" width="8" height="5" fill="none" stroke="#fff" stroke-width="1.1"/><path d="M1 2.5 L5 6 L9 2.5" fill="none" stroke="#fff" stroke-width="1.1"/></svg></span>
          mabel@mabelsfitstudio.example
        </li>
        <li class="contact-item">
          <span class="contact-icon"><svg viewBox="0 0 10 10"><circle cx="5" cy="5" r="3.8" fill="none" stroke="#fff" stroke-width="1.1"/><path d="M1.2 5 H8.8 M5 1.2 V8.8" stroke="#fff" stroke-width="1"/></svg></span>
          www.mabelsfitstudio.example
        </li>
      </ul>
    </div>
  </section>

  <section class="card card-brand" aria-label="Business card, brand side">
    <div class="brand-mark">
      <span class="brand-dot"></span>
      <span class="brand-name">Mabel’s Fitness</span>
    </div>
    <div class="tagline-band">
      <p class="tagline">Become your happiest, healthiest and strongest self</p>
    </div>
  </section>
</main>
</body>
</html>
```